Wendorf Legal: Sole Practitioner Law Firm seeking corporate branding drawing on unique bush setting

I need a logo, stationary and business card design for my law firm. I will be practising as a sole practitioner specialising in corporate, commercial, finance, migration and agriculture law. Having left my corporate job in the city and relocated our family to our farm in regional Western Australia, I would like the corporate design for my company to be crisp, stylish, concise and uncomplicated. The law firm is called "Wendorf Legal" because we have a colony of the endangered Carnaby Black Cockatoos living in the bush behind our homestead (which is also my office). I will travel to clients rather than have them visit me. I would like to see a stylised image of the bird with some Australian native bush included in the design, either as a background image on the back of the card. A separate brief has been created for the logo and stationary though I hope all 3 pieces of work will "marry". The final design should communicate clarity of vision, efficiency, compassion and solution/ outcome focused. I prefer to have the business cards printed on card with a bit of texture and substance. I will try not to use laminated card as I consider it feels "plastic and commoditised" which is inconsistent with the image and feel of the business I intend creating. Please see attached brief for further details of the design brief.

Target Market(s)

Agriculture and Horticulture companies, Farmers, Family offices and estates, banks, insurance companies, individuals wishing to migrate to Australia

Industry/Entity Type

Legal

Contact Information for Business Card

Harriet Dunbar-Kelso
LLB (Hons), BSc., MEc.
Legal Practitioner and Director

WENDORF LEGAL PTY LTD
PO Box 273, Yarrowind WA 6057
Ph: 0472 918205
Email: harrietdk@quillnet.com

Solicitor admitted to practice in the Senior Bench Tribunal of Western Australia, England and Wales, NSW, and Registered Practitioner of the Apex Bench of Australia

Logo Text

WENDORF LEGAL: Client Focused Commercial Legal Solutions

Font styles to use
Other font styles liked:
• Verlag

Colors
ec1f27
fbee3d
9bcb3c
ffffff
1b1b1b
c4c4c4

Requirements
Must have
• A look and feel of quality, conservatism, adventure
Nice to have
• A stylised image of a Carnaby Cockatoo and Australian flora as a background image or design on the back of the card.
Should not have
• Clutter, cartoons

```html
<!DOCTYPE html>
<html lang="en">
<head>
<meta charset="utf-8">
<title>Wendorf Legal – Business Card</title>
<link rel="stylesheet" href="https://fonts.googleapis.com/css2?family=Cinzel:wght@400;700&family=Open+Sans:wght@400&display=swap">
<style>
  :root {
    --navy: #12307c;
    --paper: #ffffff;
    --ink: #4a4a4a;
    --backdrop: #e9e7e3;
    --edge: #d6d3ce;
  }
  * { box-sizing: border-box; margin: 0; padding: 0; }
  html, body { width: 1200px; height: 900px; overflow: hidden; }
  body {
    background: var(--backdrop);
    position: relative;
    font-family: "Open Sans", Arial, sans-serif;
  }
  .card {
    position: absolute;
    width: 580px;
    height: 354px;
    border-radius: 4px;
    box-shadow: 0 2px 0 var(--edge), 0 10px 24px rgba(0,0,0,0.12);
  }
  .card--back {
    left: 90px; top: 80px;
    background: var(--navy);
    display: flex; align-items: center; justify-content: center;
  }
  .card--front {
    left: 530px; top: 466px;
    background: var(--paper);
    padding: 40px 46px;
  }
  .wordmark { position: relative; display: inline-block; }
  .wordmark__name {
    font-family: "Cinzel", Georgia, serif;
    font-weight: 400;
    letter-spacing: 1px;
    line-height: 1;
  }
  .wordmark__suffix {
    position: absolute; right: 2px;
    font-family: "Cinzel", Georgia, serif;
    font-size: 9px; letter-spacing: 1px;
  }
  .card--back .wordmark__name { color: var(--paper); font-size: 46px; }
  .card--back .wordmark__suffix { color: var(--paper); bottom: -16px; }
  .card--front .wordmark { margin-left: 30px; }
  .card--front .wordmark__name { color: var(--navy); font-size: 40px; }
  .card--front .wordmark__suffix { color: var(--navy); bottom: -14px; }
  .contact { margin-top: 34px; color: var(--ink); }
  .contact__name {
    font-family: "Cinzel", Georgia, serif;
    font-weight: 700; color: var(--navy);
    font-size: 19px; letter-spacing: 0.5px;
    margin-bottom: 6px;
  }
  .contact__role { font-size: 14px; line-height: 1.4; }
  .contact__lines { margin-top: 14px; font-size: 14px; line-height: 1.6; }
  .contact__line { display: flex; align-items: center; gap: 9px; }
  .contact__line svg { width: 12px; height: 12px; fill: var(--navy); }
  .contact__address { margin-top: 14px; font-size: 14px; letter-spacing: 0.2px; }
</style>
</head>
<body>
  <section class="card card--back" aria-label="Card back">
    <div class="wordmark">
      <span class="wordmark__name">Wendorf Legal</span>
      <span class="wordmark__suffix">PTY LTD</span>
    </div>
  </section>

  <section class="card card--front" aria-label="Card front">
    <div class="wordmark">
      <span class="wordmark__name">Wendorf Legal</span>
      <span class="wordmark__suffix">PTY LTD</span>
    </div>
    <div class="contact">
      <p class="contact__name">Harriet Dunbar-Kelso</p>
      <p class="contact__role">LLB (Hons), BSc., MEc.<br>Legal Practitioner and Director</p>
      <div class="contact__lines">
        <p class="contact__line">
          <svg viewBox="0 0 24 24" aria-hidden="true"><path d="M6.6 10.8a15 15 0 0 0 6.6 6.6l2.2-2.2c.3-.3.7-.4 1-.2 1.1.4 2.3.6 3.6.6.6 0 1 .4 1 1V20c0 .6-.4 1-1 1A17 17 0 0 1 3 4c0-.6.4-1 1-1h3.5c.6 0 1 .4 1 1 0 1.3.2 2.5.6 3.6.1.3 0 .7-.2 1z"/></svg>
          0472 918205
        </p>
        <p class="contact__line">
          <svg viewBox="0 0 24 24" aria-hidden="true"><path d="M2 5h20v14H2zm2 2v.5l8 5 8-5V7l-8 5z"/></svg>
          harrietdk@quillnet.com
        </p>
      </div>
      <p class="contact__address">WENDORF LEGAL PTY LTD PO Box 273, Yarrowind WA 6057</p>
    </div>
  </section>
</body>
</html>
```